A boutique/architectural website for a landscape company

I'm after a minimilstic boutique website for my landscape design and construction business. I have been exploring Wix and created some pages on that but want something more aesthetic.

Industry/Entity Type

Landscaping design and construction

Number of Pages Required

5+ page

Font styles to use
Sans Serif

Colors

Designer to choose colors to be used in the design.

Requirements
Must have
• an architectural, minimalistic look
Nice to have
• Simplicitly and nice images
Should not have
• A corporate look

```html
<!DOCTYPE html>
<html lang="en">
<head>
<meta charset="utf-8">
<title>Wattle – Landscaping &amp; Design</title>
<link href="https://fonts.googleapis.com/css2?family=Poppins:wght@200;300;400;500;600;700&family=Noto+Serif:wght@300;400;700&display=swap" rel="stylesheet">
<style>
:root{
  --green:#0b4a45;
  --green-deep:#083e3a;
  --yellow:#ffc400;
  --cream:#fefcee;
  --ink:#161616;
  --dark:#1d1b1c;
  --muted:#8fa5a2;
  --white:#ffffff;
}
*{margin:0;padding:0;box-sizing:border-box}
html,body{width:1200px;height:4835px;overflow:hidden}
body{background:var(--cream);font-family:'Poppins',sans-serif;color:var(--ink);position:relative}
.abs{position:absolute}
.serif{font-family:'Noto Serif',serif}
a{color:inherit;text-decoration:none}

/* header */
.logo{left:120px;top:0;width:119px;height:109px;background:var(--green);display:flex;align-items:center;justify-content:center;color:var(--white);font-weight:500;font-size:20px;letter-spacing:1px}
.nav{top:30px;left:322px;display:flex;gap:26px;font-size:12.5px;font-weight:500;text-transform:uppercase}
.nav .current{text-decoration:line-through}
.btn-header{left:926px;top:19px;width:154px;height:40px;background:var(--green);color:var(--white);font-size:14px;display:flex;align-items:center;justify-content:center;font-weight:500}

/* hero */
.hero-photo{left:349px;top:111px;width:731px;height:436px;background:linear-gradient(180deg,#c9d6cf 0%,#6f8a5c 40%,#8a7052 70%,#a9a39a 100%)}
.hero-title{left:120px;top:200px;font-size:34px;line-height:39px;font-weight:700;width:520px}
.hero-text{left:120px;top:314px;font-size:14px;line-height:20px;width:230px}
.btn-dark{background:var(--ink);color:var(--white);display:flex;align-items:center;justify-content:center;gap:16px;font-size:15px}
.hero-btn{left:120px;top:413px;width:256px;height:45px}
.socials{left:120px;top:524px;display:flex;gap:26px}
.socials span{width:22px;height:22px;border:2px solid var(--ink);border-radius:50%}
.slide-cur{left:872px;top:478px;font-size:52px;font-weight:300;color:var(--white)}
.slide-total{left:872px;top:570px;font-size:52px;font-weight:300;color:var(--green)}
.arrow-box{background:var(--green);display:flex;align-items:center;justify-content:center;gap:8px}
.hero-arrows{left:960px;top:548px;width:120px;height:109px}

/* about */
.about{left:0;top:657px;width:1200px;height:406px;background:var(--green)}
.band{left:0;top:1063px;width:1200px;height:51px;background:var(--yellow)}
.section-title{font-size:34px;font-weight:600;letter-spacing:2px;text-align:center;width:1200px;left:0}
.underline{width:62px;height:3px;left:569px}
.about-title{top:718px;color:var(--white)}
.about-line{top:774px;background:var(--white)}
.about-text{left:351px;top:813px;width:498px;font-size:13.5px;line-height:20px;color:var(--white)}
.enlarge{left:0;width:1200px;top:969px;text-align:center;font-size:13px;font-style:italic;color:var(--muted)}
.gallery{top:1006px;width:214px;height:196px}
.g1{left:244px;background:linear-gradient(160deg,#2f5a2a,#6c8e43 55%,#a06a3a)}
.g2{left:492px;background:linear-gradient(180deg,#2e2a26,#6d5a44 50%,#3a3430)}
.g3{left:742px;background:linear-gradient(180deg,#a7b6c2,#5c6b5a 55%,#5d4533)}
.btn-yellow{background:var(--yellow);color:var(--ink);display:flex;align-items:center;justify-content:center;font-size:14px;font-weight:500;letter-spacing:1px}
.view-more{left:515px;top:1247px;width:170px;height:45px}

/* dots */
.dots{display:grid;gap:0}
.dots span{width:8px;height:8px;background:var(--muted)}

/* video */
.video{left:240px;top:1384px;width:720px;height:366px;background:linear-gradient(180deg,#b7bcbf,#8c9295 50%,#5c554c)}
.play{left:548px;top:1516px}

/* how it works */
.how-title{top:1848px}
.how-line{top:1900px;background:var(--ink)}
.step{width:240px;text-align:left}
.step-num{font-size:104px;font-weight:200;color:transparent;-webkit-text-stroke:1.3px #b9c3c2;line-height:1;top:1958px}
.step-title{top:2107px;font-size:13.5px;font-weight:600}
.step-day{top:2175px;font-size:13px;font-weight:500}
.step-text{top:2220px;font-size:13px;line-height:19px;width:230px}
.timeline{left:343px;top:2157px;width:506px;height:1px;background:#b9c3c2}
.tdot{top:2146px;width:24px;height:24px;border-radius:50%;background:var(--yellow);border:2px solid var(--green)}

/* packages */
.pkg-card{left:120px;top:2445px;width:359px;height:547px;background:var(--white)}
.pkg-photo{left:479px;top:2445px;width:601px;height:547px;background:linear-gradient(160deg,#4b5a48,#2d3b2a 40%,#3f6b32 70%,#7a4a34)}
.pkg-title{left:507px;top:2398px;font-size:54px;font-weight:700;letter-spacing:3px}
.pkg-name{left:167px;top:2478px;font-size:15px;font-weight:500}
.pkg-price{left:167px;top:2512px;font-size:19px;font-weight:600}
.pkg-icon{top:2551px;width:44px;height:44px;border-radius:50%;background:var(--green)}
.pkg-feat{left:167px;font-size:13.5px;font-weight:500;display:flex;align-items:center;gap:10px}
.pkg-text{left:167px;top:2786px;font-size:13px;line-height:19px;width:230px}
.pkg-more{left:167px;top:2920px;font-size:14px;font-weight:500;color:var(--green);border-bottom:1px solid var(--green)}
.pkg-tab{top:2932px;font-size:15px;color:rgba(255,255,255,.5)}
.pkg-tab.active{color:var(--white);font-weight:600}
.pkg-arrows{left:960px;top:2885px;width:120px;height:107px}

/* testimonials */
.test-title{top:3086px}
.test-line{top:3140px;background:var(--ink)}
.quote{font-size:70px;font-weight:700;color:var(--green);font-family:'Noto Serif',serif;line-height:1}
.test-text{left:361px;top:3184px;width:472px;font-size:13.5px;line-height:20px}
.test-dash{left:644px;top:3313px;width:42px;height:1px;background:var(--ink)}
.test-author{left:702px;top:3298px;font-size:12.5px;line-height:17px}
.pager{top:3355px;width:11px;height:11px;border-radius:50%;border:1.5px solid var(--green)}

/* faq */
.faq{left:0;top:3456px;width:1200px;height:587px;background:var(--green)}
.faq-title{top:3525px;color:var(--white)}
.faq-item{left:308px;width:582px;height:57px;display:flex;align-items:center;justify-content:space-between;padding:0 40px 0 60px;font-size:13.5px;font-weight:500;background:var(--white);border:1px solid #d9d9d9}
.faq-item.open{background:var(--yellow);border-color:var(--yellow)}
.faq-answer{left:368px;top:3709px;width:470px;font-size:13px;line-height:20px;color:var(--white)}

/* cta */
.cta-photo{left:0;top:4043px;width:1200px;height:286px;background:linear-gradient(90deg,#c9b8a4,#e6ddd0 35%,#ece4d8 60%,#b9a690)}
.cta-title{left:0;width:1200px;top:4104px;text-align:center;font-size:29px;line-height:38px;font-weight:700}
.cta-btn{left:471px;top:4224px;width:256px;height:45px}
.ask{left:0;width:1200px;top:4390px;text-align:center;font-size:21px;font-weight:600}
.contact-btn{left:515px;top:4458px;width:170px;height:45px}

/* footer */
.footer{left:0;top:4567px;width:1200px;height:268px;background:var(--dark);color:var(--white)}
.footer-contact{top:4634px;font-size:14px;font-weight:600}
.footer-nav{top:4710px;font-size:13px;font-weight:500;text-transform:uppercase}
.footer-rule{top:4719px;width:46px;height:1px;background:#8a8a8a}
.footer-social{top:4707px;width:24px;height:24px;border-radius:50%;border:2px solid var(--white)}
.copyright{left:0;width:1200px;top:4799px;text-align:center;font-size:12.5px;color:#777}
</style>
</head>
<body>

<header>
  <div class="abs logo">Wattle</div>
  <nav class="abs nav">
    <a class="current">Home</a><a>How it works</a><a>Packages</a><a>Portofolio</a><a>About us</a><a>Contact</a>
  </nav>
  <a class="abs btn-header">Start Project</a>
</header>

<section class="hero">
  <div class="abs hero-photo" role="img" aria-label="Rooftop terrace with wooden lounge sofas, planters and trees"></div>
  <h1 class="abs hero-title serif">Time To Change Your Outdoors Is Right Now</h1>
  <p class="abs hero-text">Lorem ipsum dolor sit amet, consetetur sadipscing elitr, sed diam nonumy eirmod</p>
  <a class="abs hero-btn btn-dark">Start Your Project
    <svg width="38" height="10" viewBox="0 0 38 10"><path d="M0 5h36M31 1l5 4-5 4" stroke="#fff" fill="none" stroke-width="1.2"/></svg></a>
  <div class="abs socials"><span></span><span></span><span></span></div>
  <div class="abs slide-cur serif">01</div>
  <div class="abs slide-total serif">04</div>
  <div class="abs hero-arrows arrow-box">
    <svg width="78" height="52" viewBox="0 0 78 52"><path d="M28 2L6 26l22 24M50 2l22 24-22 24" stroke="#fff" fill="none" stroke-width="2"/></svg>
  </div>
</section>

<section class="about-section">
  <div class="abs about"></div>
  <div class="abs band"></div>
  <h2 class="abs section-title about-title">ABOUT&nbsp; WATTLE</h2>
  <div class="abs underline about-line"></div>
  <p class="abs about-text">Lorem ipsum dolor sit amet, consetetur sadipscing elitr, sed diam nonumy eirmod tempor invidunt ut labore et dolore magna aliquyam erat, sed diam voluptua. At vero eos et accusam et justo duo dolores et ea rebum. Stet clita kasd gubergren, no sea takimata sanctus est Lorem ipsum dolor sit amet. Lorem ipsum dolor sit amet, consetetur</p>
  <p class="abs enlarge">Click on the Images to Enlarge</p>
  <svg class="abs" style="left:186px;top:1064px" width="30" height="50" viewBox="0 0 30 50"><path d="M26 2L4 25l22 23" stroke="#0b4a45" fill="none" stroke-width="2"/></svg>
  <div class="abs gallery g1" role="img" aria-label="Garden lounge chairs among lush tropical plants"></div>
  <div class="abs gallery g2" role="img" aria-label="Pergola with curtains and string lights at dusk"></div>
  <div class="abs gallery g3" role="img" aria-label="Hillside patio with wicker chairs overlooking a valley"></div>
  <svg class="abs" style="left:984px;top:1064px" width="30" height="50" viewBox="0 0 30 50"><path d="M4 2l22 23-22 23" stroke="#0b4a45" fill="none" stroke-width="2"/></svg>
  <a class="abs view-more btn-yellow">VIEW MORE</a>
</section>

<div class="abs dots" style="left:120px;top:1310px;grid-template-columns:repeat(4,8px);column-gap:40px;row-gap:39px">
  <span></span><span></span><span></span><span></span>
  <span></span><span></span><span></span><span></span>
  <span></span><span></span><span></span><span style="opacity:0"></span>
  <span></span><span></span><span></span><span style="opacity:0"></span>
</div>

<section class="video-section">
  <div class="abs video" role="img" aria-label="Patio with lounge chairs and potted plants beside a grey clad wall"></div>
  <svg class="abs play" width="104" height="104" viewBox="0 0 104 104" aria-label="Play video">
    <circle cx="52" cy="52" r="50" fill="#fff"/><path d="M40 30l34 22-34 22z" fill="#0b4a45"/>
  </svg>
</section>

<div class="abs dots" style="left:840px;top:1672px;grid-template-columns:repeat(4,8px);column-gap:40px;row-gap:39px">
  <span style="opacity:0"></span><span style="opacity:0"></span><span style="opacity:0"></span><span></span>
  <span style="opacity:0"></span><span style="opacity:0"></span><span style="opacity:0"></span><span></span>
  <span></span><span></span><span></span><span></span>
  <span></span><span></span><span></span><span></span>
</div>

<section class="how">
  <h2 class="abs section-title how-title">HOW IT WORKS</h2>
  <div class="abs underline how-line"></div>
  <div class="abs step step-num" style="left:312px">1</div>
  <div class="abs step step-num" style="left:566px">2</div>
  <div class="abs step step-num" style="left:816px">3</div>
  <div class="abs step step-title" style="left:240px">Tell Us Whats On Your Mind</div>
  <div class="abs step step-title" style="left:497px">Refining The Design Concept</div>
  <div class="abs step step-title" style="left:755px">Construction &amp; Planting</div>
  <div class="abs timeline"></div>
  <div class="abs tdot" style="left:331px"></div>
  <div class="abs tdot" style="left:588px"></div>
  <div class="abs tdot" style="left:837px"></div>
  <div class="abs step-day" style="left:320px">1 DAY</div>
  <div class="abs step-day" style="left:572px">3 DAYS</div>
  <div class="abs step-day" style="left:804px">2 - 3 WEEKS</div>
  <p class="abs step step-text" style="left:240px">Lorem ipsum dolor sit amet, consetetur sadipscing elitr, sed diam nonumy eirmod tempor</p>
  <p class="abs step step-text" style="left:497px">Lorem ipsum dolor sit amet, consetetur sadipscing elitr, sed diam nonumy eirmod tempor</p>
  <p class="abs step step-text" style="left:755px">Lorem ipsum dolor sit amet, consetetur sadipscing elitr, sed diam nonumy eirmod tempor</p>
</section>

<div class="abs dots" style="left:95px;top:2415px;grid-template-columns:repeat(4,8px);column-gap:40px;row-gap:39px">
  <span></span><span></span><span></span><span></span>
  <span></span><span style="opacity:0"></span><span style="opacity:0"></span><span style="opacity:0"></span>
  <span></span><span style="opacity:0"></span><span style="opacity:0"></span><span style="opacity:0"></span>
  <span></span><span style="opacity:0"></span><span style="opacity:0"></span><span style="opacity:0"></span>
</div>

<section class="packages">
  <div class="abs pkg-card"></div>
  <div class="abs pkg-photo" role="img" aria-label="Front yard with lawn, brick house and outdoor dining chairs"></div>
  <h2 class="abs pkg-title">PACKAGES</h2>
  <div class="abs pkg-name">Front Yard Design &amp; Construction</div>
  <div class="abs pkg-price">1000 $ - 1500 $</div>
  <div class="abs pkg-icon" style="left:167px"></div>
  <div class="abs pkg-icon" style="left:226px"></div>
  <div class="abs pkg-feat" style="top:2644px">
    <svg width="24" height="24" viewBox="0 0 24 24"><circle cx="12" cy="12" r="10" fill="none" stroke="#777" stroke-width="1.5"/><path d="M12 6v6l4 2" stroke="#777" fill="none" stroke-width="1.5"/></svg>2-3 WEEKS</div>
  <div class="abs pkg-feat" style="top:2686px;gap:6px">
    <svg width="14" height="14" viewBox="0 0 14 14"><path d="M1 8l4 4 8-11" stroke="#0b4a45" fill="none" stroke-width="1.6"/></svg>Landscape Design &amp; Construction</div>
  <div class="abs pkg-feat" style="top:2720px;gap:6px">
    <svg width="14" height="14" viewBox="0 0 14 14"><path d="M1 8l4 4 8-11" stroke="#0b4a45" fill="none" stroke-width="1.6"/></svg>Planting &amp; Gardening</div>
  <p class="abs pkg-text">Lorem ipsum dolor sit amet, consetetur sadipscing elitr, sed diam nonumy eirmod tempor invidunt ut labore et dolore</p>
  <a class="abs pkg-more">More Details</a>
  <span class="abs pkg-tab" style="left:524px">Full Yard</span>
  <span class="abs pkg-tab" style="left:627px">Back Yard</span>
  <span class="abs pkg-tab active" style="left:740px">Front Yard</span>
  <div class="abs pkg-arrows arrow-box">
    <svg width="78" height="52" viewBox="0 0 78 52"><path d="M28 2L6 26l22 24M50 2l22 24-22 24" stroke="#fff" fill="none" stroke-width="2"/></svg>
  </div>
</section>

<div class="abs dots" style="left:968px;top:3008px;grid-template-columns:repeat(3,8px);column-gap:40px;row-gap:39px">
  <span></span><span></span><span></span>
  <span></span><span></span><span></span>
</div>

<section class="testimonials">
  <h2 class="abs section-title test-title">TESTIMONIALS</h2>
  <div class="abs underline test-line"></div>
  <div class="abs quote" style="left:298px;top:3152px">"</div>
  <div class="abs quote" style="left:864px;top:3226px">"</div>
  <p class="abs test-text">Lorem ipsum dolor sit amet, consetetur sadipscing elitr, sed diam nonumy eirmod tempor invidunt ut labore et dolore magna aliquyam erat, sed diam voluptua. At vero eos et accusam et justo duo dolores et ea rebum. Stet clita kasd gubergren, no sea takimata sanctus est</p>
  <div class="abs test-dash"></div>
  <div class="abs test-author">Lorem ipsum dolor<br>sit amet, consetetur</div>
  <div class="abs pager" style="left:569px"></div>
  <div class="abs pager" style="left:593px;background:var(--green)"></div>
  <div class="abs pager" style="left:617px"></div>
</section>

<section class="faq-section">
  <div class="abs faq"></div>
  <h2 class="abs section-title faq-title">FAQ SECTION</h2>
  <div class="abs faq-item open" style="top:3609px">How Long Does The Whole Process Take ?
    <svg width="36" height="18" viewBox="0 0 36 18"><path d="M1 16L18 2l17 14" stroke="#0b4a45" fill="none" stroke-width="1.5"/></svg></div>
  <p class="abs faq-answer">Lorem ipsum dolor sit amet, consetetur sadipscing elitr, sed diam nonum eirmod tempor invidunt ut labore et dolore or sit nonumy</p>
  <div class="abs faq-item" style="top:3806px">What Services Do You Provide ?
    <svg width="36" height="18" viewBox="0 0 36 18"><path d="M1 2l17 14L35 2" stroke="#0b4a45" fill="none" stroke-width="1.5"/></svg></div>
  <div class="abs faq-item" style="top:3900px">Does Revisions Affect the Price ?
    <svg width="36" height="18" viewBox="0 0 36 18"><path d="M1 2l17 14L35 2" stroke="#0b4a45" fill="none" stroke-width="1.5"/></svg></div>
</section>

<section class="cta">
  <div class="abs cta-photo" role="img" aria-label="Faded courtyard with brick walls, plants and rustic furniture"></div>
  <h2 class="abs cta-title serif">Our Team of Top Designers Will Design<br>Your Outdoors For You</h2>
  <a class="abs cta-btn btn-dark">Start Your Project
    <svg width="38" height="10" viewBox="0 0 38 10"><path d="M0 5h36M31 1l5 4-5 4" stroke="#fff" fill="none" stroke-width="1.2"/></svg></a>
  <p class="abs ask">If You Have Any Questions Feel Free To Ask</p>
  <a class="abs contact-btn btn-yellow">CONTACT US</a>
</section>

<footer>
  <div class="abs footer"></div>
  <div class="abs footer-contact" style="left:341px;color:#fff">Email :&nbsp;&nbsp; hello@wattlegardens.com</div>
  <div class="abs footer-contact" style="left:649px;color:#fff">Phone :&nbsp;&nbsp; + 61 300 555 019</div>
  <a class="abs footer-nav" style="left:120px;color:#fff">Home</a>
  <a class="abs footer-nav" style="left:198px;color:#fff">How it works</a>
  <a class="abs footer-nav" style="left:342px;color:#fff">Packages</a>
  <div class="abs footer-rule" style="left:453px"></div>
  <div class="abs footer-social" style="left:525px"></div>
  <div class="abs footer-social" style="left:588px"></div>
  <div class="abs footer-social" style="left:648px"></div>
  <div class="abs footer-rule" style="left:703px"></div>
  <a class="abs footer-nav" style="left:777px;color:#fff">Portofolio</a>
  <a class="abs footer-nav" style="left:907px;color:#fff">About us</a>
  <a class="abs footer-nav" style="left:1016px;color:#fff">Contact</a>
  <p class="abs copyright">WATTLE - Landscaping &amp; Design. 2021 © All Rights Reserved</p>
</footer>

</body>
</html>
```